Unique Beautiful Realtor business card

I need a unique business card that includes my logo, my firms logo, my picture and phone number. The colors should compliment my logo.

Target Market(s)

People who want to buy or sell a home in South Florida

Contact Information for Business Card

Use two sides and work with the DRM Coastal Homes logo as a theme.
The Harlow Benton should be small and discreet, it is a requirement to be there but should be small. My photo should be integrated artistically.

Font styles to use
Serif
Sans Serif

Colors

Designer to choose colors to be used in the design.

Requirements
Must have
• My logo, Harlow Benton logo, my photo, my phone number, (954-283-6091) and my website address. (www.drmcoastalhomes.example)
• Also my name, Dana R. Moreland, PA, Realtor
• Also “The Home-Loving Realtor”

```html
<!DOCTYPE html>
<html lang="en">
<head>
<meta charset="utf-8">
<title>Dana R. Moreland – Business Card</title>
<link rel="stylesheet" href="https://fonts.googleapis.com/css2?family=Montserrat:wght@400;500;600;700&display=swap">
<style>
  :root {
    --backdrop: #d6d5d6;
    --olive: #56592a;
    --lime: #9aab2a;
    --paper: #ffffff;
    --ink: #4a4a4a;
    --photo-sky: #e9ece6;
    --photo-mid: #8c8f6e;
    --photo-low: #3b3f3a;
  }
  * { margin: 0; padding: 0; box-sizing: border-box; }
  html, body { width: 1200px; height: 900px; overflow: hidden; }
  body {
    background: var(--backdrop);
    font-family: "Montserrat", sans-serif;
    position: relative;
  }
  .card {
    position: absolute;
    left: 277px;
    width: 645px;
    height: 368px;
    background: var(--paper);
    box-shadow: 0 6px 14px rgba(0,0,0,0.28);
    overflow: hidden;
  }
  .card--front { top: 65px; }
  .card--back { top: 466px; }
  .card svg.card__art { position: absolute; inset: 0; }

  .identity { position: absolute; line-height: 1; white-space: nowrap; }
  .identity__name { font-size: 20px; font-weight: 700; letter-spacing: 0.3px; }
  .identity__name .surname { font-weight: 500; color: var(--lime); }
  .identity__role { font-size: 17px; font-weight: 500; margin-top: 9px; }
  .identity__tagline { font-size: 17px; font-weight: 500; color: var(--lime); margin-top: 9px; }

  .card--front .identity { left: 384px; top: 177px; width: 250px; text-align: center; color: var(--paper); }

  .card--back .identity { right: 40px; top: 116px; text-align: right; color: var(--ink); }
  .card--back .identity__name { color: var(--ink); }
  .card--back .identity__role, .card--back .identity__tagline { font-size: 16px; margin-top: 6px; }
  .identity__rule { height: 2px; background: var(--lime); width: 216px; margin: 9px 0 0 auto; }

  .contact { position: absolute; right: 38px; top: 208px; text-align: right; color: var(--ink); font-size: 16.5px; font-weight: 500; white-space: nowrap; }
  .contact__line { display: flex; justify-content: flex-end; align-items: center; gap: 9px; height: 24px; }
  .contact__line .accent { color: var(--lime); }
  .contact__icon { width: 15px; height: 15px; }

  .brand { position: absolute; left: 30px; top: 196px; color: var(--paper); white-space: nowrap; }
  .brand__mark { display: flex; align-items: center; gap: 9px; }
  .brand__dot { width: 14px; height: 14px; border-radius: 50%; background: var(--lime); flex: none; }
  .brand__name { font-size: 20px; font-weight: 600; letter-spacing: 0.4px; line-height: 1.15; }
  .brand__firm { margin-top: 26px; margin-left: 62px; font-size: 12px; font-weight: 600; letter-spacing: 1px; }
</style>
</head>
<body>

<section class="card card--front" aria-label="Front of card">
  <svg class="card__art" width="645" height="368" viewBox="0 0 645 368">
    <defs>
      <linearGradient id="photoTone" x1="0" y1="0" x2="0" y2="1">
        <stop offset="0" stop-color="var(--photo-sky)"/>
        <stop offset="0.55" stop-color="var(--photo-mid)"/>
        <stop offset="1" stop-color="var(--photo-low)"/>
      </linearGradient>
    </defs>
    <polygon points="125,0 475,0 283,368 0,368 0,172" fill="url(#photoTone)" role="img" aria-label="Portrait photo of the realtor outdoors by a lakeside home"/>
    <polygon points="0,0 120,0 0,165" fill="var(--olive)"/>
    <polygon points="120,0 128,0 0,176 0,165" fill="var(--lime)"/>
    <polygon points="475,0 645,0 645,368 283,368" fill="var(--olive)"/>
    <polygon points="475,0 485,0 293,368 283,368" fill="var(--lime)"/>
  </svg>
  <div class="identity">
    <p class="identity__name">DANA R. <span class="surname">MORELAND</span></p>
    <p class="identity__role">PA | Realtor</p>
    <p class="identity__tagline">“The Home-Loving Realtor”</p>
  </div>
</section>

<section class="card card--back" aria-label="Back of card">
  <svg class="card__art" width="645" height="368" viewBox="0 0 645 368">
    <polygon points="0,0 443,0 206,368 0,368" fill="var(--olive)"/>
    <polygon points="443,0 452,0 215,368 206,368" fill="var(--lime)"/>
    <polygon points="645,270 645,368 580,368" fill="var(--olive)"/>
    <polygon points="645,258 645,270 580,368 568,368" fill="var(--lime)"/>
  </svg>

  <div class="brand">
    <div class="brand__mark">
      <span class="brand__dot"></span>
      <span class="brand__name">DRM COASTAL HOMES</span>
    </div>
    <p class="brand__firm">HARLOW BENTON</p>
  </div>

  <div class="identity">
    <p class="identity__name">DANA R. <span class="surname">MORELAND</span></p>
    <p class="identity__role">PA | Realtor</p>
    <p class="identity__tagline">“The Home-Loving Realtor”</p>
    <div class="identity__rule"></div>
  </div>

  <div class="contact">
    <p class="contact__line">954 283 6091
      <svg class="contact__icon" viewBox="0 0 24 24" aria-hidden="true"><path fill="var(--lime)" d="M6.6 10.8a15.1 15.1 0 0 0 6.6 6.6l2.2-2.2a1 1 0 0 1 1-.25 11.4 11.4 0 0 0 3.6.57 1 1 0 0 1 1 1V20a1 1 0 0 1-1 1A17 17 0 0 1 3 4a1 1 0 0 1 1-1h3.5a1 1 0 0 1 1 1c0 1.25.2 2.45.57 3.6a1 1 0 0 1-.25 1z"/></svg>
    </p>
    <p class="contact__line"><span>www.<span class="accent">drmcoastalhomes</span>.example</span>
      <svg class="contact__icon" viewBox="0 0 24 24" aria-hidden="true"><circle cx="12" cy="12" r="10" fill="var(--lime)"/><path d="M2 12h20M12 2c3 3 3 17 0 20M12 2c-3 3-3 17 0 20" stroke="var(--paper)" stroke-width="1.5" fill="none"/></svg>
    </p>
  </div>
</section>

</body>
</html>
```